Business Card Design Project

I have a two letter domain name qo.com.au (lower case font please). I want a business card, cum logo that is die cut (around the qo segment at least) that fits standard business card size.
qo is all about what 'I am' - a journalist, blogger, analyst, commentator. My mantra is "I wander so qo'.
The reverse of the card only needs my name Lon Fitch, email lon@qo.com.au and mobile +61 400 555 817
Target Market(s)
Mainly people that will use my professional writing services and suppliers that will provide product for review
Industry/Entity Type
Business
Requirements
Must have
- One side is qo.com.au (hint - the .com.au can be vertical or horizontal to fit - the qo should be as large as possible).
The other requires large size font name, email and phone details (so no one needs glasses to read it).
The die cut can be just to highlight the qo segment - need not be around the whole card.
Font used in the past was Belwe (old style - very much like the i used in the information symbol).
Colours - no preference - prefer two colour to process colour but can also be an outline font instead of solid colour.

```html
<!DOCTYPE html>
<html lang="en">
<head>
<meta charset="utf-8">
<title>Lon Fitch — Business Card Options</title>
<link rel="stylesheet" href="https://fonts.googleapis.com/css2?family=Anton&family=Arimo:wght@400;700&family=Rokkitt:wght@400;800&display=swap">
<style>
  :root {
    --sheet: #ffffff;
    --sheet-edge: #6e6e6e;
    --card-edge: #3a3a3a;
    --charcoal: #404040;
    --graphite: #262626;
    --cut: #000000;
    --amber: #ffba00;
    --cyan: #00f0f0;
    --silver: #bdbdbd;
    --ink: #1a1a1a;
    --ink-soft: #444444;
    --slate: #3d3d3d;
    --white: #ffffff;
    --dash: #cfcfcf;
  }
  * { margin: 0; padding: 0; box-sizing: border-box; }
  html, body { width: 1200px; height: 1188px; overflow: hidden; background: var(--sheet); }
  .sheet {
    position: relative; width: 1230px; height: 1218px;
    transform: scale(0.97561); transform-origin: 0 0;
    border: 2px solid var(--sheet-edge); background: var(--sheet);
  }
  .side-label {
    position: absolute; top: 70px; width: 527px; text-align: center;
    font-family: Arimo, Arial, sans-serif; font-weight: 400; font-size: 22px; color: var(--ink);
  }
  .side-label.front { left: 77px; }
  .side-label.back { left: 618px; }
  .card {
    position: absolute; width: 527px; height: 301px; overflow: hidden;
    border: 1px solid var(--card-edge);
  }
  .card svg.cutouts { position: absolute; inset: 0; width: 527px; height: 301px; }
  .col-front { left: 77px; }
  .col-back { left: 618px; }
  .row-1 { top: 120px; background: var(--charcoal); }
  .row-2 { top: 475px; background: var(--white); border-color: #888; }
  .row-3 { top: 832px; background: var(--graphite); }
  .txt { position: absolute; white-space: nowrap; line-height: 1; }
  .centered { transform: translateX(-50%); text-align: center; }
  .slab { font-family: Rokkitt, Georgia, serif; font-weight: 800; }
  .contact-sans { font-family: Arimo, Arial, sans-serif; font-weight: 700; font-size: 24px; color: var(--white); }
  .contact-serif { font-family: Rokkitt, Georgia, serif; font-weight: 400; font-size: 24px; color: var(--ink-soft); letter-spacing: 0.5px; }
  .condensed { font-family: Anton, Impact, sans-serif; font-weight: 400; }
  .domain-name { font-size: 56px; }
  .illustration { position: absolute; border-radius: 60px 60px 30px 30px; }
</style>
</head>
<body>
<div class="sheet">
  <div class="side-label front">FRONT PRINT</div>
  <div class="side-label back">BACK PRINT</div>

  <!-- Option 1 — charcoal with amber slash -->
  <section class="card row-1 col-front">
    <svg class="cutouts" viewBox="0 0 527 301" aria-hidden="true">
      <path d="M95,0 H139 V160 Z" fill="var(--amber)"/>
      <polygon points="280,0 386,0 333,73" fill="var(--cut)"/>
      <polygon points="226,225 226,301 294,301" fill="var(--cut)"/>
      <polygon points="439,225 439,301 371,301" fill="var(--cut)"/>
    </svg>
    <div class="txt centered slab" style="left:336px;top:98px;font-size:56px;color:var(--amber);">Lon Fitch</div>
    <div class="txt centered contact-sans" style="left:336px;top:162px;">lon@qo.com.au</div>
    <div class="txt centered contact-sans" style="left:336px;top:191px;">+61 400 555 817</div>
  </section>

  <section class="card row-1 col-back">
    <svg class="cutouts" viewBox="0 0 527 301" aria-hidden="true">
      <path d="M387,0 H432 L387,160 Z" fill="var(--amber)"/>
      <polygon points="142,0 248,0 194,73" fill="var(--cut)"/>
      <polygon points="89,225 89,301 157,301" fill="var(--cut)"/>
      <polygon points="300,225 300,301 232,301" fill="var(--cut)"/>
    </svg>
    <div class="txt centered slab domain-name" style="left:195px;top:118px;color:var(--silver);">qo.com.au</div>
  </section>

  <!-- Option 2 — white with curved die cuts -->
  <section class="card row-2 col-front">
    <svg class="cutouts" viewBox="0 0 527 301" aria-hidden="true">
      <path d="M278,0 Q333,0 333,70 Q333,0 388,0 Z" fill="var(--cut)"/>
      <path d="M188,301 Q226,301 226,230 Q226,301 264,301 Z" fill="var(--cut)"/>
      <path d="M401,301 Q439,301 439,230 Q439,301 477,301 Z" fill="var(--cut)"/>
    </svg>
    <div class="illustration" role="img" aria-label="Amber and black lightbulb pencil illustration"
         style="left:42px;top:42px;width:132px;height:222px;background:linear-gradient(180deg,var(--amber) 0 58%,var(--ink) 58% 92%,var(--amber) 92%);"></div>
    <div class="txt centered condensed" style="left:331px;top:84px;font-size:56px;color:var(--ink);">Lon Fitch</div>
    <div class="txt centered contact-serif" style="left:331px;top:160px;">lon@qo.com.au</div>
    <div class="txt centered contact-serif" style="left:331px;top:189px;">+61 400 555 817</div>
  </section>

  <section class="card row-2 col-back">
    <svg class="cutouts" viewBox="0 0 527 301" aria-hidden="true">
      <path d="M139,0 Q194,0 194,70 Q194,0 249,0 Z" fill="var(--cut)"/>
      <path d="M51,301 Q89,301 89,230 Q89,301 127,301 Z" fill="var(--cut)"/>
      <path d="M262,301 Q300,301 300,230 Q300,301 338,301 Z" fill="var(--cut)"/>
    </svg>
    <div class="txt centered slab domain-name" style="left:194px;top:118px;color:var(--slate);">qo.com.au</div>
    <div class="illustration" role="img" aria-label="Dark grey lightbulb pencil illustration"
         style="left:373px;top:62px;width:110px;height:184px;background:linear-gradient(180deg,var(--slate),#2a2a2a);"></div>
  </section>

  <!-- Option 3 — graphite with cyan name -->
  <section class="card row-3 col-front">
    <svg class="cutouts" viewBox="0 0 527 301" aria-hidden="true">
      <polygon points="280,0 386,0 333,73" fill="var(--cut)"/>
      <polygon points="226,225 226,301 294,301" fill="var(--cut)"/>
      <polygon points="439,225 439,301 371,301" fill="var(--cut)"/>
      <line x1="139" y1="228" x2="139" y2="285" stroke="var(--dash)" stroke-width="2" stroke-dasharray="8 8"/>
    </svg>
    <div class="txt condensed" style="left:38px;top:30px;font-size:112px;color:var(--cyan);letter-spacing:1px;">LON</div>
    <div class="txt condensed" style="left:38px;top:140px;font-size:76px;color:var(--cyan);">FITCH</div>
    <div class="txt contact-sans" style="left:277px;top:118px;">lon@qo.com.au</div>
    <div class="txt contact-sans" style="left:277px;top:149px;">+61 400 555 817</div>
  </section>

  <section class="card row-3 col-back">
    <svg class="cutouts" viewBox="0 0 527 301" aria-hidden="true">
      <polygon points="142,0 248,0 194,73" fill="var(--cut)"/>
      <polygon points="89,225 89,301 157,301" fill="var(--cut)"/>
      <polygon points="300,225 300,301 232,301" fill="var(--cut)"/>
      <line x1="387" y1="188" x2="387" y2="285" stroke="var(--dash)" stroke-width="2" stroke-dasharray="8 8"/>
    </svg>
    <div class="txt centered slab" style="left:262px;top:124px;font-size:40px;color:var(--white);letter-spacing:1px;">I wander so qo'</div>
  </section>
</div>
</body>
</html>
```